Louisiana personal injury attorney needs a postcard design

This will be the first of three post cards to go out to previous clients. We do not have intentions of making all three match/work with each other, but if you have an idea for that, please, let us know! This is for an attorney in Lafayette, LA that specializes in Medical Malpractice and Personal Injury. We would like the front of the post card to focus on those two practice areas and really grab someones attention!

the card in general will say: Glad to have served you, come see us for a free T-shirt, have a cup of coffee with us…

Please use a photo of the office for us to use on the back with a map of the office location (will send location when we pick the winner)

Industry/Entity Type

Legal

Font styles to use
Serif
Sans Serif

Requirements
Must have
• map of location of office. Large image or several images on the front. attention grabbing
Nice to have
• colors that match the logo. clean and easy to follow
Should not have
• should not be messy or too much going on.

```html
<!DOCTYPE html>
<html lang="en">
<head>
<meta charset="utf-8">
<title>Marlow Law Firm — Postcard</title>
<link href="https://fonts.googleapis.com/css2?family=Montserrat:wght@300;400;500;600;700;800&display=swap" rel="stylesheet">
<style>
  :root {
    --gold: #c9972f;
    --charcoal: #5c5c5e;
    --ink: #2b2b2b;
    --paper: #ffffff;
    --mist: #eeeeee;
    --page: #ececec;
    --rule: #d9d9d9;
  }
  * { box-sizing: border-box; margin: 0; padding: 0; }
  html, body { width: 783px; height: 1200px; overflow: hidden; }
  body {
    background: var(--page);
    font-family: "Montserrat", Arial, sans-serif;
    color: var(--ink);
    position: relative;
  }
  .postcard {
    position: absolute;
    left: 28px;
    width: 765px;
    height: 510px;
    background: linear-gradient(90deg, var(--mist) 0%, var(--paper) 70%);
    box-shadow: 0 4px 10px rgba(0,0,0,.25);
    transform: scale(0.95);
    transform-origin: top left;
    overflow: hidden;
  }
  .postcard--front { top: 90px; }
  .postcard--back { top: 625px; background: linear-gradient(90deg, var(--paper) 0%, #f7f7f7 100%); }

  .shapes { position: absolute; inset: 0; width: 765px; height: 510px; }
  .shapes .gold { fill: var(--gold); }
  .shapes .charcoal { fill: var(--charcoal); }
  .shapes .paper { fill: var(--paper); }

  .photo { position: absolute; inset: 0; }
  .photo--clinic {
    background: linear-gradient(160deg, #e6e9ec 0%, #9fb8cc 35%, #3f86c4 55%, #dfe3e6 80%, #c7cdd2 100%);
    clip-path: polygon(610px 48px, 765px 292px, 765px 450px, 382px 450px);
  }
  .photo--office {
    background: linear-gradient(180deg, #cfdbe6 0%, #9fb0bf 25%, #3f4248 45%, #34363b 75%, #5d7a3a 92%, #7a8a62 100%);
    clip-path: polygon(0 205px, 372px 205px, 293px 455px, 0 455px);
  }
  .map-spot {
    position: absolute;
    left: 375px; top: 428px; width: 125px; height: 27px;
    background: linear-gradient(90deg, #eef0f2, #dfe6ec);
    border: 1px solid #b9bec4;
  }

  .brand-name {
    position: absolute;
    left: 30px; top: 46px;
    font-size: 31px; font-weight: 700;
    letter-spacing: 1px;
    color: var(--gold);
    white-space: nowrap;
  }
  .brand-name--small {
    left: 475px; top: 128px;
    font-size: 12px;
    letter-spacing: .3px;
  }

  .headline { position: absolute; left: 30px; line-height: 1; }
  .headline__lead {
    display: block;
    font-weight: 400;
    font-size: 44px;
    color: var(--ink);
    letter-spacing: .3px;
  }
  .headline__accent {
    display: block;
    font-weight: 700;
    font-size: 31px;
    color: var(--gold);
    letter-spacing: 1px;
    line-height: 1.18;
    margin-top: 6px;
  }
  .headline--front { top: 138px; }
  .headline--back { top: 28px; }
  .headline--back .headline__lead { font-size: 37px; }
  .headline--back .headline__accent { font-size: 23px; margin-top: 2px; }

  .short-rule {
    position: absolute; left: 32px; top: 270px;
    width: 80px; height: 3px; background: var(--ink);
  }
  .focus-box {
    position: absolute; left: 30px; top: 292px;
    width: 400px; height: 93px;
    background: var(--gold);
  }
  .focus-box__text {
    position: absolute; left: 52px; top: 314px;
    width: 340px;
    color: var(--paper);
    font-size: 14px; font-weight: 500;
    line-height: 1.35;
    white-space: nowrap;
  }
  .invite {
    position: absolute; left: 33px; top: 404px;
    width: 290px;
    font-size: 10px; line-height: 1.3;
    color: var(--ink);
    white-space: nowrap;
  }

  .about {
    position: absolute; left: 28px; top: 103px;
    width: 348px;
    font-size: 8.3px; line-height: 1.28;
    text-align: justify;
    color: var(--ink);
  }
  .cta-strip {
    position: absolute; left: 0; top: 189px;
    width: 368px; height: 16px;
    background: var(--gold);
    color: var(--paper);
    font-size: 8px;
    line-height: 16px;
    padding-left: 36px;
    white-space: nowrap;
  }

  .stamp-box {
    position: absolute; left: 638px; top: 85px;
    width: 78px; height: 85px;
    background: #e7e7e7;
  }
  .address-line {
    position: absolute; left: 475px;
    width: 240px; height: 1px;
    background: var(--rule);
  }

  .contact {
    position: absolute;
    display: flex; align-items: center; gap: 8px;
    color: var(--paper);
    white-space: nowrap;
  }
  .contact svg { fill: none; stroke: var(--paper); stroke-width: 2; }
  .contact--phone { left: 30px; top: 460px; height: 45px; font-size: 28px; font-weight: 500; letter-spacing: .5px; }
  .contact--place { top: 462px; height: 40px; font-size: 14px; font-weight: 500; line-height: 1.2; }
  .contact--web { top: 462px; height: 40px; font-size: 14px; font-weight: 500; }
  .postcard--front .contact--place { left: 375px; }
  .postcard--front .contact--web { left: 580px; }
  .postcard--back .contact--place { left: 335px; }
  .postcard--back .contact--web { left: 580px; }
</style>
</head>
<body>

<section class="postcard postcard--front" aria-label="Postcard front">
  <svg class="shapes" viewBox="0 0 765 510" aria-hidden="true">
    <rect class="charcoal" x="0" y="455" width="765" height="55"/>
  </svg>
  <div class="focus-box"></div>
  <svg class="shapes" viewBox="0 0 765 510" aria-hidden="true">
    <polygon class="gold" points="565,0 655,0 765,172 765,455 362,455 330,510 265,510"/>
    <polygon class="paper" points="610,32 765,275 765,455 372,455"/>
  </svg>
  <div class="photo photo--clinic" role="img" aria-label="Photo: medical team in scrubs and white coats reviewing a scan on a tablet, seen from above"></div>

  <div class="brand-name">MARLOW LAW FIRM</div>

  <h1 class="headline headline--front">
    <span class="headline__lead">Experienced</span>
    <span class="headline__accent">LOUISIANA PERSONAL<br>INJURY ATTORNEYS</span>
  </h1>
  <div class="short-rule"></div>
  <p class="focus-box__text">This is for an attorney in Lafayette<br>LA that specializes in Medical Malpractice<br>and Personal Injury.</p>
  <p class="invite">Glad to have served you, Come see us for a free<br>T-shirt,&nbsp; have a cup of coffee with us</p>

  <div class="contact contact--phone">
    <svg width="22" height="22" viewBox="0 0 24 24"><path d="M5 3h4l2 5-2.5 1.5a11 11 0 0 0 6 6L16 13l5 2v4a2 2 0 0 1-2 2A17 17 0 0 1 3 5a2 2 0 0 1 2-2z"/></svg>
    <span>337-555-0148</span>
  </div>
  <div class="contact contact--place">
    <svg width="16" height="22" viewBox="0 0 16 22"><path d="M8 21s-6-7-6-12a6 6 0 0 1 12 0c0 5-6 12-6 12z"/><circle cx="8" cy="9" r="2"/></svg>
    <span>220 Magnolia Court<br>Lafayette, LA 70508</span>
  </div>
  <div class="contact contact--web">
    <svg width="18" height="18" viewBox="0 0 20 20"><circle cx="10" cy="10" r="8"/><path d="M2 10h16M10 2c3 3 3 13 0 16M10 2c-3 3-3 13 0 16"/></svg>
    <span>www.marlowlaw.com</span>
  </div>
</section>

<section class="postcard postcard--back" aria-label="Postcard back">
  <div class="photo photo--office" role="img" aria-label="Photo: the firm's dark two-storey office building with glass windows and trees"></div>
  <svg class="shapes" viewBox="0 0 765 510" aria-hidden="true">
    <rect class="charcoal" x="0" y="455" width="765" height="55"/>
    <polygon class="gold" points="445,0 475,0 310,510 270,510"/>
  </svg>
  <div class="map-spot" role="img" aria-label="Map showing the office location"></div>

  <h2 class="headline headline--back">
    <span class="headline__lead">Dedicated To</span>
    <span class="headline__accent">HELPING INJURED PEOPLE</span>
  </h2>
  <p class="about">At Marlow Law Firm, in Lafayette, we represent people who have suffered personal injuries as well as surviving family members of wrongful death victims. Serious accidents can occur in nearly every facet of life, from work to driving to using a power tool to simply crossing the street. It is crucial to hold the responsible parties accountable for their negligence or inattention to safety. We will vigorously fight on our clients' behalf through all phases of the legal process.</p>
  <div class="cta-strip">Please contact our law office online today to schedule a free consultation.</div>

  <div class="brand-name brand-name--small">MARLOW LAW FIRM</div>
  <div class="stamp-box"></div>
  <div class="address-line" style="top:228px"></div>
  <div class="address-line" style="top:268px"></div>
  <div class="address-line" style="top:307px"></div>
  <div class="address-line" style="top:345px"></div>

  <div class="contact contact--phone">
    <svg width="22" height="22" viewBox="0 0 24 24"><path d="M5 3h4l2 5-2.5 1.5a11 11 0 0 0 6 6L16 13l5 2v4a2 2 0 0 1-2 2A17 17 0 0 1 3 5a2 2 0 0 1 2-2z"/></svg>
    <span>337-555-0148</span>
  </div>
  <div class="contact contact--place">
    <svg width="16" height="22" viewBox="0 0 16 22"><path d="M8 21s-6-7-6-12a6 6 0 0 1 12 0c0 5-6 12-6 12z"/><circle cx="8" cy="9" r="2"/></svg>
    <span>220 Magnolia Court<br>Lafayette, LA 70508</span>
  </div>
  <div class="contact contact--web">
    <svg width="18" height="18" viewBox="0 0 20 20"><circle cx="10" cy="10" r="8"/><path d="M2 10h16M10 2c3 3 3 13 0 16M10 2c-3 3-3 13 0 16"/></svg>
    <span>www.marlowlaw.com</span>
  </div>
</section>

</body>
</html>
```